Unique E-commerce website needs a FLAT UI design

Looking for creative website designer / company to design a flat ui interface for the main 4 pages.

I SEEK FLAT UI DESIGN ONLY - this means nice, clean and modern design,

As we're dealing with the design of the main pages this will define the overall site design so take a moment or two to think on the audience and create an appealing branding.

Website design must be mobile/ipad friendly.

I've written a detailed design requirements document for those 4 pages.
Please read it carefully and make sure you understand every aspect of it before starting the design process.
You can find a brief intro text and some reference designs that I like to get you started.

This is not a closed concept, I'm open to hear new ideas and ways to improve the UI/UX.

Feel free to ask anything, I'm available most of the day.

I'm looking to build a long term relationship as this is the first phase of the design, I have 1-2 phases to come.

Target Market(s)

Online shoppers age between 18-60 that buy frequently at US merchants

Industry/Entity Type

It Company

Number of Pages Required

4 page

Requirements
Must have
• Flat UI design
• Flat colors
• Modern, clean and easy to follow design
Nice to have
• Original icons for the features page

```html
<!DOCTYPE html>
<html lang="en">
<head>
<meta charset="utf-8">
<title>Shipnest Home – We Made Shipping Simple</title>
<link href="https://fonts.googleapis.com/css2?family=Baumans&family=Lato:ital,wght@0,400;0,700;1,400;1,700&family=Ubuntu:wght@400;500&display=swap" rel="stylesheet">
<style>
:root{
  --red:#e84c3d;
  --red-dark:#c8402f;
  --orange:#f39c12;
  --orange-ring:#f5b04a;
  --blue:#2b7fc0;
  --blue-title:#2a78b8;
  --blue-dark:#22639a;
  --navy:#1f3d5a;
  --grey-band:#c9d1d4;
  --card:#f1f1f1;
  --text:#555b60;
  --text-light:#8a9095;
  --white:#ffffff;
}
*{box-sizing:border-box;margin:0;padding:0}
html,body{width:1200px;height:2396px;overflow:hidden}
body{font-family:"Lato",sans-serif;color:var(--text);background:var(--white);position:relative}
.wrap{width:880px;margin:0 auto;position:relative}

/* top bar */
.topbar{height:40px;background:var(--white)}
.topbar .wrap{display:flex;align-items:center;height:40px;font-size:10px;color:var(--text)}
.topbar .info{display:flex;align-items:center;gap:8px;margin-right:22px}
.topbar .ico{width:18px;height:18px;border:1px solid var(--blue);border-radius:3px;display:flex;align-items:center;justify-content:center}
.topbar .auth{margin-left:auto;display:flex;gap:8px}
.topbar .auth span{border:1px solid #b9bec2;border-radius:2px;padding:2px 10px;font-size:10px}

/* header */
.header{height:88px;background:var(--red)}
.header .wrap{display:flex;align-items:center;height:88px}
.logo{display:flex;align-items:center;gap:12px;font-family:"Lato",sans-serif;font-weight:700;font-size:22px;color:var(--white);letter-spacing:.5px}
.logo .mark{width:34px;height:34px;border-radius:50%;background:var(--white)}
.nav{margin-left:auto;display:flex;gap:36px}
.nav a{color:var(--white);text-decoration:none;font-size:14px;display:flex;flex-direction:column;align-items:center;gap:6px;width:58px}
.nav svg{width:26px;height:26px}

/* hero */
.hero{height:452px;position:relative;overflow:hidden}
.hero .photo{position:absolute;inset:0;background:linear-gradient(90deg,#6c645c 0%,#4d4a48 35%,#5a4f44 65%,#8a6a48 100%)}
.hero .shade{position:absolute;inset:0;background:rgba(20,18,16,.25)}
.hero .copy{position:absolute;left:394px;top:168px;color:var(--white)}
.hero h1{font-family:"Baumans",sans-serif;font-weight:400;font-size:36px;letter-spacing:1px}
.hero h2{font-family:"Baumans",sans-serif;font-weight:400;font-size:25px;margin-top:8px}
.hero h2 em{color:var(--orange);font-style:normal}
.hero .btn{display:inline-block;margin-top:22px;border:2px solid var(--orange);color:var(--orange);font-size:14px;padding:8px 8px;background:rgba(0,0,0,.15)}

/* section heads */
.sec-head{text-align:center}
.sec-head h3{font-family:"Baumans",sans-serif;font-weight:400;font-size:24px;color:var(--blue-title)}
.sec-head p{font-size:14px;color:var(--text-light);margin-top:10px}
.sec-head .rule{width:340px;height:1px;background:#d9dcde;margin:12px auto 0;position:relative}
.sec-head .rule::after{content:"";position:absolute;left:110px;top:-1px;width:120px;height:2px;background:#8d9398}

/* what we do */
.services{height:386px;padding-top:40px}
.services .cols{display:flex;justify-content:space-between;width:880px;margin:40px auto 0;padding:0 26px}
.service{width:260px;text-align:center}
.service .ring{width:106px;height:106px;border-radius:50%;border:2px solid var(--orange-ring);margin:0 auto;display:flex;align-items:center;justify-content:center}
.service .ring .inner{width:90px;height:90px;border-radius:50%;border:1px solid #f0d7b4;display:flex;align-items:center;justify-content:center}
.service h4{font-size:19px;font-weight:400;color:var(--navy);margin-top:20px}
.service p{font-size:12px;line-height:18px;color:#3a3f44;margin-top:6px}

/* pricing */
.pricing{height:540px;background:var(--grey-band);padding-top:44px}
.pricing .sec-head p{color:#6f767b}
.cards{display:flex;justify-content:space-between;width:844px;margin:32px auto 0}
.card{width:250px;height:332px;background:var(--card);position:relative;box-shadow:0 14px 14px -10px rgba(0,0,0,.25)}
.card .cap{height:38px;color:var(--white);font-size:17px;display:flex;align-items:center;justify-content:center;box-shadow:0 2px 0 rgba(0,0,0,.2)}
.card ul{list-style:none;padding:20px 30px 0 20px}
.card li{display:flex;gap:12px;font-size:14px;line-height:19px;color:#4a4f54;min-height:47px}
.card li svg{flex:none;width:22px;height:20px;margin-top:-2px}
.card .btn{position:absolute;left:10px;right:10px;bottom:14px;height:32px;color:var(--white);font-family:"Ubuntu",sans-serif;font-size:12px;display:flex;align-items:center;justify-content:center;box-shadow:0 2px 0 rgba(0,0,0,.2)}
.red{background:var(--red)}.orange{background:var(--orange)}.blue{background:var(--blue)}

/* offers */
.offers{height:264px;position:relative;overflow:hidden}
.offers .photo{position:absolute;inset:0;background:linear-gradient(90deg,#c4483c 0%,#cf5446 50%,#d8705f 75%,#c9493d 100%)}
.offer{position:absolute;top:32px;height:214px;border:1px solid rgba(255,255,255,.35);color:var(--white);text-align:center;display:flex;flex-direction:column;justify-content:center}
.offer::after{content:"";position:absolute;inset:6px;border:1px solid rgba(255,255,255,.25)}
.offer strong{font-family:"Baumans",sans-serif;font-weight:400;font-size:54px;line-height:1;margin-bottom:4px}
.offer span{font-family:"Baumans",sans-serif;font-weight:400;font-size:20px;line-height:30px}

/* brands */
.brands{height:256px;padding-top:46px}
.brand-row{display:flex;justify-content:space-between;width:886px;margin:34px auto 0}
.brand{width:172px;height:76px;border:1px solid #e2e5e7;display:flex;align-items:center;justify-content:center;font-family:"Lato",sans-serif;font-weight:700;font-size:20px;color:var(--blue-dark);white-space:nowrap}

/* get started */
.cta{height:134px;background:var(--orange)}
.cta .wrap{display:flex;align-items:center;height:134px}
.cta h3{font-family:"Baumans",sans-serif;font-weight:400;font-size:28px;color:var(--white)}
.cta p{font-size:13px;font-style:italic;font-weight:700;color:#fff6e6;line-height:19px;margin-top:6px;width:560px}
.cta .btn{margin-left:auto;margin-right:40px;width:228px;height:46px;background:var(--blue);color:var(--white);font-family:"Ubuntu",sans-serif;font-size:18px;display:flex;align-items:center;justify-content:center;box-shadow:0 2px 0 var(--blue-dark)}

/* footer */
.footer{height:212px;background:var(--blue);color:var(--white);padding-top:32px}
.footer .wrap{display:flex}
.fcol h5{font-size:14px;font-weight:400;padding-bottom:8px;border-bottom:1px solid rgba(255,255,255,.35);width:130px;margin-bottom:12px}
.fcol{font-size:10px;line-height:13px}
.overview{width:264px}.overview .links{display:grid;grid-template-columns:120px 120px;row-gap:14px}
.contact{width:238px}.contact .row{display:flex;gap:8px;margin-bottom:12px}
.contact svg{flex:none;width:12px;height:12px}
.newsletter{width:242px}
.newsletter .field{width:168px;height:20px;background:var(--white);color:#888;font-size:8px;padding:5px 6px;margin-top:8px}
.newsletter .sub{display:inline-block;background:var(--red);font-size:9px;padding:4px 8px;margin-top:8px}
.social .row{display:flex;align-items:center;gap:8px;margin-bottom:10px}
.social .dot{width:18px;height:18px;border-radius:50%;background:var(--white)}
.bottombar{position:absolute;left:0;right:0;bottom:0;height:26px;background:var(--blue-dark);color:var(--white);font-size:10px}
.bottombar .wrap{display:flex;align-items:center;height:26px}
.bottombar .pay{margin-left:auto;margin-right:14px;font-weight:700;font-size:14px}
</style>
</head>
<body>

<div class="topbar">
  <div class="wrap">
    <div class="info"><span class="ico"><svg width="10" height="12" viewBox="0 0 10 12"><path d="M5 0a4 4 0 0 0-4 4c0 3 4 8 4 8s4-5 4-8a4 4 0 0 0-4-4z" fill="#2b7fc0"/></svg></span>Lorem ipsum dolor sit amet concuer</div>
    <div class="info"><span class="ico"><svg width="11" height="11" viewBox="0 0 12 12"><path d="M2 1l3 0 1 3-2 1a7 7 0 0 0 3 3l1-2 3 1v3c-6 0-9-3-9-9z" fill="#2b7fc0"/></svg></span>Call Us:- 555-210-3344</div>
    <div class="auth"><span>Sign in ▾</span><span>Sign up</span></div>
  </div>
</div>

<header class="header">
  <div class="wrap">
    <div class="logo"><span class="mark"></span>SHIPNEST HOME</div>
    <nav class="nav">
      <a href="#"><svg viewBox="0 0 26 26" fill="none" stroke="#fff" stroke-width="2"><rect x="5" y="4" width="16" height="19"/><path d="M9 10h8M9 14h8M9 18h5"/></svg>Features</a>
      <a href="#"><svg viewBox="0 0 26 26" fill="none" stroke="#fff" stroke-width="2"><path d="M14 3h9v9L12 23 3 14z"/><circle cx="18" cy="8" r="2"/></svg>Pricing</a>
      <a href="#"><svg viewBox="0 0 26 26" fill="none" stroke="#fff" stroke-width="2"><circle cx="13" cy="13" r="10"/><path d="M13 11v7M13 7v1"/></svg>Help</a>
      <a href="#"><svg viewBox="0 0 26 26" fill="none" stroke="#fff" stroke-width="2"><path d="M2 7h14v11H2zM16 11h5l3 4v3h-8z"/><circle cx="7" cy="20" r="2" fill="#e84c3d"/><circle cx="19" cy="20" r="2" fill="#e84c3d"/></svg>Shipping</a>
    </nav>
  </div>
</header>

<section class="hero">
  <div class="photo" role="img" aria-label="Smiling businessman holding a clipboard in a busy warehouse"></div>
  <div class="shade"></div>
  <div class="copy">
    <h1>WE MADE SHIPPING SIMPLE</h1>
    <h2>WITH <em>SHIPNEST HOME</em> IS YOUR NEW 24/7 POST OFFICE.</h2>
    <span class="btn">Rapid Account Creation</span>
  </div>
</section>

<section class="services">
  <div class="sec-head">
    <h3>WHAT WE DO</h3>
    <p>Ut wisi enim ad minim veniam, quis nostrud exerci tation ullamcorper</p>
    <div class="rule"></div>
  </div>
  <div class="cols">
    <div class="service">
      <div class="ring"><div class="inner"><svg width="48" height="36" viewBox="0 0 48 36"><rect x="2" y="6" width="28" height="20" fill="#e84c3d"/><path d="M30 12h9l7 8v6H30z" fill="#e84c3d"/><circle cx="12" cy="29" r="5" fill="#e84c3d" stroke="#fff" stroke-width="2"/><circle cx="37" cy="29" r="5" fill="#e84c3d" stroke="#fff" stroke-width="2"/></svg></div></div>
      <h4>Ship it Over</h4>
      <p>Lorem ipsum dolor sit amet, consectetuer adipiscing elit, sed diam nonummy nibh euismod tincidunt ut laoreet dolore magna aliquam</p>
    </div>
    <div class="service">
      <div class="ring"><div class="inner"><svg width="40" height="46" viewBox="0 0 40 46"><rect x="12" y="4" width="6" height="40" fill="#e84c3d"/><rect x="4" y="4" width="32" height="5" fill="#e84c3d"/><path d="M32 9v10" stroke="#e84c3d" stroke-width="2"/><rect x="28" y="19" width="8" height="8" fill="#e84c3d"/><rect x="6" y="38" width="18" height="6" fill="#e84c3d"/></svg></div></div>
      <h4>We&nbsp; do the heavy lifting</h4>
      <p>Lorem ipsum dolor sit amet, consectetuer adipiscing elit, sed diam nonummy nibh euismod tincidunt ut laoreet dolore magna aliquam</p>
    </div>
    <div class="service">
      <div class="ring"><div class="inner"><svg width="44" height="44" viewBox="0 0 44 44"><path d="M4 12l12-4 12 4 12-4v26l-12 4-12-4-12 4z" fill="none" stroke="#e84c3d" stroke-width="3"/><path d="M22 6a7 7 0 0 0-7 7c0 6 7 13 7 13s7-7 7-13a7 7 0 0 0-7-7z" fill="#e84c3d"/><circle cx="22" cy="13" r="2.5" fill="#fff"/></svg></div></div>
      <h4>Track delivery</h4>
      <p>Lorem ipsum dolor sit amet, consectetuer adipiscing elit, sed diam nonummy nibh euismod tincidunt ut laoreet dolore magna aliquam</p>
    </div>
  </div>
</section>

<section class="pricing">
  <div class="sec-head">
    <h3>OUR PRICING</h3>
    <p>There are no hidden fees and no surprises at checkout</p>
    <div class="rule"></div>
  </div>
  <div class="cards">
    <div class="card">
      <div class="cap red">Package Related</div>
      <ul>
        <li><svg viewBox="0 0 22 20"><path d="M2 10l6 7L20 2" fill="none" stroke="#d62b2b" stroke-width="3"/></svg>Package Processing $1</li>
        <li><svg viewBox="0 0 22 20"><path d="M2 10l6 7L20 2" fill="none" stroke="#d62b2b" stroke-width="3"/></svg>Payment Processing 4% of shipping costs</li>
        <li><svg viewBox="0 0 22 20"><path d="M2 10l6 7L20 2" fill="none" stroke="#d62b2b" stroke-width="3"/></svg>Package Consolidation starting from $2</li>
        <li><svg viewBox="0 0 22 20"><path d="M2 10l6 7L20 2" fill="none" stroke="#d62b2b" stroke-width="3"/></svg>Storage $1</li>
      </ul>
      <div class="btn red">SIGN UP FOR FREE</div>
    </div>
    <div class="card">
      <div class="cap orange">Extra Services</div>
      <ul>
        <li><svg viewBox="0 0 22 20"><path d="M2 10l6 7L20 2" fill="none" stroke="#e8a31a" stroke-width="3"/></svg>Content photos starting from $2</li>
        <li><svg viewBox="0 0 22 20"><path d="M2 10l6 7L20 2" fill="none" stroke="#e8a31a" stroke-width="3"/></svg>Repacking $5</li>
        <li><svg viewBox="0 0 22 20"><path d="M2 10l6 7L20 2" fill="none" stroke="#e8a31a" stroke-width="3"/></svg>Filling Out Customs Form $5</li>
        <li><svg viewBox="0 0 22 20"><path d="M2 10l6 7L20 2" fill="none" stroke="#e8a31a" stroke-width="3"/></svg>Express Checkout $5</li>
        <li><svg viewBox="0 0 22 20"><path d="M2 10l6 7L20 2" fill="none" stroke="#e8a31a" stroke-width="3"/></svg>Custom Requests $5</li>
      </ul>
      <div class="btn orange">LEARN MORE</div>
    </div>
    <div class="card">
      <div class="cap blue">Surcharges</div>
      <ul>
        <li><svg viewBox="0 0 22 20"><path d="M2 10l6 7L20 2" fill="none" stroke="#2b6fb8" stroke-width="3"/></svg>Missing Mailbox Number $2</li>
        <li><svg viewBox="0 0 22 20"><path d="M2 10l6 7L20 2" fill="none" stroke="#2b6fb8" stroke-width="3"/></svg>Heavy Package $10</li>
        <li><svg viewBox="0 0 22 20"><path d="M2 10l6 7L20 2" fill="none" stroke="#2b6fb8" stroke-width="3"/></svg>Return Label Processing $5</li>
        <li><svg viewBox="0 0 22 20"><path d="M2 10l6 7L20 2" fill="none" stroke="#2b6fb8" stroke-width="3"/></svg>diam nonummy nibh</li>
      </ul>
      <div class="btn blue">LEARN MORE</div>
    </div>
  </div>
</section>

<section class="offers">
  <div class="photo" role="img" aria-label="Blurred piggy bank and stacked coins in warm red tones"></div>
  <div class="offer" style="left:182px;width:396px"><strong>10% OFF</strong><span>For Ordering More Than 1 Service</span></div>
  <div class="offer" style="left:624px;width:400px"><strong>15% OFF</strong><span>On Ordering Extra Service<br>For Every Incoming Package.</span></div>
</section>

<section class="brands">
  <div class="sec-head">
    <h3 style="color:var(--blue-dark)">US BRANDS</h3>
    <p>Ut wisi enim ad minim veniam, quis nostrud exerci tation ullamcorper</p>
    <div class="rule"></div>
  </div>
  <div class="brand-row">
    <div class="brand">Maplemart</div>
    <div class="brand">Bidloft</div>
    <div class="brand">Denvik</div>
    <div class="brand">rivermarket.com</div>
    <div class="brand">tinytots</div>
  </div>
</section>

<section class="cta">
  <div class="wrap">
    <div>
      <h3>GET STARTED</h3>
      <p>Lorem ipsum dolor sit amet, consectetuer adipiscing elit, sed diam nonummy nibh euismod tincidunt ut laoreet dolore magna aliquam erat volutpat.</p>
    </div>
    <div class="btn">GET STARTED NOW</div>
  </div>
</section>

<footer class="footer">
  <div class="wrap">
    <div class="fcol overview">
      <h5>Overview</h5>
      <div class="links"><span>Feature</span><span>About Us</span><span>Pricing</span><span>Contact Us</span><span>Package Calculator</span><span></span><span>Rivermarket Calculator</span></div>
    </div>
    <div class="fcol contact">
      <h5>Contact Address</h5>
      <div class="row"><svg viewBox="0 0 12 12"><path d="M6 0a4 4 0 0 0-4 4c0 3 4 8 4 8s4-5 4-8a4 4 0 0 0-4-4z" fill="#fff"/></svg><span><b>Lorem ipsum dolor sit amet,</b><br>consectetuer adipiscing elit,<br>sed diam nonummy nibh</span></div>
      <div class="row"><svg viewBox="0 0 12 12"><path d="M2 1h3l1 3-2 1a7 7 0 0 0 3 3l1-2 3 1v3C5 10 2 7 2 1z" fill="#fff"/></svg><span>0555-210-334</span></div>
      <div class="row"><svg viewBox="0 0 12 12"><rect x="1" y="2" width="10" height="8" fill="none" stroke="#fff"/><path d="M1 2l5 4 5-4" fill="none" stroke="#fff"/></svg><span>support@shipnesthome.com</span></div>
    </div>
    <div class="fcol newsletter">
      <h5>Newsletter Signup</h5>
      <div>Signup with us and get update in<br>your inbox.</div>
      <div class="field">Your Name</div>
      <div class="field">Email address</div>
      <span class="sub">Subscribe</span>
    </div>
    <div class="fcol social">
      <h5>Social Connect</h5>
      <div class="row"><span class="dot"></span>Friendwall</div>
      <div class="row"><span class="dot"></span>Chirpline</div>
      <div class="row"><span class="dot"></span>Workgraph</div>
    </div>
  </div>
</footer>
<div class="bottombar">
  <div class="wrap"><span>Copyright © 2014 - Shipnest Home</span><span class="pay">PayWise</span></div>
</div>

</body>
</html>
```